Australian Legal Practice would like a Web Design

I need a web design for a newly established law practice operating as Brindell Legal.

I would like the business to have an internet presence (via a website) essentially for the purpose of marketing and advertising. As the business grows (hopefully) I may be interested in providing general legal information as a means of establishing goodwill in the community and a easy and user friends contact method through the website.

The essence of the business is personal legal service based on local knowledge and therefore i want the website to present a picture of friendly professionalism, but mostly i want people who to be able to find the contact details of the business

I would like to have a map of the office location, and photos of the front of the office, the staff (me at the moment) and picture of law themed items and featuring the Brindell Legal logo.

The areas of law which Brindell Legal practises in are as follows:

commercial law
business sale and purchases
leases
conveyancing and property law
wills and estates
powers of attorney
general legal advice
succession planning
Updates

Target Market(s)

Potential and existing clients of the firm
Other law firms
Associated stakeholders, i.e. Banks and real estate agents

Industry/Entity Type

Law Firm

Coding

Coded - Design and coding required

Number of Pages Required

2 page

Font styles to use
Sans Serif

Colors
85acd3
33a6d7
0456a4

Requirements
Must have
• Brindell Legal logo
• Map of the office location
• Picture of Ross Kedwick (principal solicitor)
• Picture of the office
• Areas of Practice
• Address of office
• email address: ross.kedwick@brindelllegal-example.com.au
• Physical address: 17 Pellow Road, Hamilton VIC 3300
• Phone number: (03) 5598 4731
• Facsimile number: (03) 5598 4706
• Space for a brief description of the firm and its competitive advantage
• Bar Guild Logo
• Links to the Bar Guild of Victoria
• Link to the practitioner oversight Council
Nice to have
• coded to wordpress format

```html
<!DOCTYPE html>
<html lang="en">
<head>
<meta charset="utf-8">
<title>Brindell Legal</title>
<link rel="stylesheet" href="https://fonts.googleapis.com/css2?family=Open+Sans:wght@400;600;700;800&display=swap">
<style>
  :root{
    --navy:#0456a4;
    --nav:#1e6db6;
    --sky:#33a6d7;
    --powder:#85acd3;
    --band:#7ea8d3;
    --ink:#1f2b3a;
    --muted:#6b7280;
    --line:#dfe5ec;
    --paper:#ffffff;
    --soft:#f4f6f9;
  }
  *{box-sizing:border-box;margin:0;padding:0}
  html,body{width:1200px;height:2304px;overflow:hidden}
  body{font-family:"Open Sans",Arial,sans-serif;color:var(--ink);background:var(--paper);position:relative}

  /* Header */
  .site-header{height:108px;display:flex;align-items:center;justify-content:space-between;padding:0 72px}
  .brand{display:flex;align-items:center;gap:10px;font-weight:700;font-size:28px;color:var(--navy);letter-spacing:.5px}
  .brand-mark{width:14px;height:14px;background:var(--navy)}
  .header-contact{display:flex;flex-direction:column;gap:8px;font-size:14px;color:var(--ink)}
  .header-contact .phone{font-size:17px;font-weight:600}
  .header-contact div{display:flex;align-items:center;gap:10px}
  .header-contact svg{flex:none}

  /* Navigation */
  .main-nav{height:40px;background:var(--nav);display:flex;align-items:stretch;padding-left:72px}
  .main-nav a{color:#fff;text-decoration:none;font-size:12px;font-weight:700;letter-spacing:.4px;display:flex;align-items:center;padding:0 17px}
  .main-nav a.active{background:var(--sky)}

  /* Hero */
  .hero{position:relative;height:472px}
  .hero-photo{position:absolute;inset:0;background:linear-gradient(120deg,#5a4a3c 0%,#2f4150 35%,#3d5466 60%,#8a7a66 100%)}
  .contact-panel{position:absolute;right:48px;top:40px;width:290px;background:rgba(20,40,60,.55);padding:0 0 16px}
  .contact-panel h2{background:var(--sky);color:#fff;font-size:15px;font-weight:700;padding:10px 14px;letter-spacing:.5px}
  .contact-panel form{padding:14px 14px 0;display:flex;flex-direction:column;gap:10px}
  .field{background:#fff;height:30px;font-size:12px;color:#8a8f98;padding:0 10px;display:flex;align-items:center}
  .field.message{height:48px;align-items:flex-start;padding-top:8px}
  .submit{align-self:flex-end;background:var(--navy);color:#fff;font-size:12px;font-weight:700;padding:9px 18px;letter-spacing:.4px}

  /* Welcome */
  .welcome{text-align:center;padding:44px 150px 0;height:232px}
  .section-title{font-size:22px;font-weight:700;color:var(--navy);letter-spacing:.5px}
  .welcome p{margin:16px auto 0;font-size:13px;line-height:1.75;color:var(--muted)}
  .btn{display:inline-block;background:var(--sky);color:#fff;font-size:11px;font-weight:700;padding:9px 22px;letter-spacing:.4px;margin-top:22px}

  /* Practice areas */
  .practice{background:var(--band);height:376px;padding-top:34px;margin-top:8px}
  .practice-title{display:flex;align-items:center;justify-content:center;gap:10px;color:#fff;font-size:22px;font-weight:700;letter-spacing:1px}
  .cards{display:flex;justify-content:center;gap:32px;margin-top:34px}
  .card{width:282px;background:#fff;padding:24px 26px 22px;text-align:center;height:230px}
  .card h3{font-size:13px;font-weight:700;color:var(--navy);margin-top:12px}
  .card p{font-size:12px;line-height:1.6;color:var(--muted);margin-top:10px}
  .card .more{display:block;font-size:11px;font-weight:700;color:var(--navy);margin-top:14px}

  /* Team and gallery */
  .team-gallery{display:flex;gap:52px;padding:40px 72px 0;height:520px}
  .team,.gallery{flex:1}
  .col-title{font-size:20px;font-weight:700;color:var(--ink);letter-spacing:.5px;margin-bottom:22px}
  .member{display:flex;gap:18px;margin-bottom:26px}
  .member-photo{width:92px;height:92px;flex:none;background:linear-gradient(160deg,#c9b8a6,#8a7565)}
  .member h4{font-size:13px;font-weight:700;color:var(--navy);margin-top:6px}
  .member p{font-size:12px;line-height:1.6;color:var(--muted);margin-top:6px}
  .gallery-grid{display:grid;grid-template-columns:1fr 1fr;grid-template-rows:170px 176px;gap:10px}
  .g1{background:linear-gradient(135deg,#3c3430,#7c6a58)}
  .g2{background:linear-gradient(135deg,#c9c2b8,#7f8f9e)}
  .g3{background:linear-gradient(135deg,#d8dde4,#6e8aa8)}
  .g4{background:linear-gradient(135deg,#e8e3d8,#9d8f7a)}

  /* Map */
  .map{position:absolute;left:0;top:1760px;width:1200px;height:260px;background:linear-gradient(180deg,#eceae4,#dcdad2)}
  .map-pin{position:absolute;left:572px;top:1846px}

  /* Office band */
  .office{position:absolute;left:0;top:2020px;width:1200px;height:160px;background:var(--sky);color:#fff;text-align:center;padding-top:36px}
  .office h2{font-size:22px;font-weight:700;letter-spacing:1px}
  .office-details{display:flex;justify-content:center;gap:34px;margin-top:28px;font-size:12px}
  .office-details span{display:flex;align-items:center;gap:8px}

  /* Footer */
  .site-footer{position:absolute;left:0;top:2180px;width:1200px;height:124px;display:flex;justify-content:space-between;align-items:center;padding:0 72px}
  .site-footer .brand{font-size:22px}
  .legal{font-size:11px;color:var(--muted);margin-top:8px;line-height:1.6}
  .follow{display:flex;align-items:center;gap:10px;font-size:12px;color:var(--ink)}
  .social{width:26px;height:26px;background:var(--navy)}
  .social.s2{background:var(--sky)}
  .social.s3{background:var(--powder)}
</style>
</head>
<body>

<header class="site-header">
  <div class="brand"><span class="brand-mark"></span>Brindell Legal</div>
  <div class="header-contact">
    <div class="phone">
      <svg width="16" height="16" viewBox="0 0 24 24"><path fill="#0456a4" d="M6.6 10.8a15 15 0 006.6 6.6l2.2-2.2a1 1 0 011-.25 11.4 11.4 0 003.6.57 1 1 0 011 1V20a1 1 0 01-1 1A17 17 0 013 4a1 1 0 011-1h3.5a1 1 0 011 1c0 1.25.2 2.45.57 3.57a1 1 0 01-.25 1z"/></svg>
      (03) 5598 4731
    </div>
    <div>
      <svg width="16" height="12" viewBox="0 0 24 18"><rect width="24" height="18" fill="#0456a4"/><path d="M1 1l11 9 11-9" stroke="#fff" stroke-width="2" fill="none"/></svg>
      ross.kedwick@brindelllegal-example.com.au
    </div>
  </div>
</header>

<nav class="main-nav">
  <a class="active">HOME</a><a>ABOUT US</a><a>PRACTICE AREA</a><a>OUR TEAM</a><a>NEWS UPDATES</a><a>BLOG</a><a>TESTIMONIALS</a><a>CAREERS</a><a>CONTACT US</a>
</nav>

<section class="hero">
  <div class="hero-photo" role="img" aria-label="Photo of a chalkboard asking if you need a lawyer, on a wooden desk"></div>
  <aside class="contact-panel">
    <h2>CONTACT US</h2>
    <form>
      <div class="field">Name</div>
      <div class="field">Email Address</div>
      <div class="field">Contact No</div>
      <div class="field">Subject</div>
      <div class="field message">Message</div>
      <div class="submit">SUBMIT NOW</div>
    </form>
  </aside>
</section>

<section class="welcome">
  <h1 class="section-title">WELCOME TO OUR WEBSITE</h1>
  <p>Brindell Legal is a local practice in Hamilton offering friendly, professional advice to families and businesses across the Western District. We combine careful attention to detail with local knowledge, clear fees and prompt replies, so every client understands their options and feels supported from the first meeting to the final result of their matter.</p>
  <span class="btn">READ MORE</span>
</section>

<section class="practice">
  <h2 class="practice-title">
    <svg width="22" height="22" viewBox="0 0 24 24"><circle cx="12" cy="12" r="10" fill="none" stroke="#fff" stroke-width="2"/><circle cx="12" cy="12" r="4" fill="#fff"/></svg>
    PRACTICE AREAS
  </h2>
  <div class="cards">
    <article class="card">
      <svg width="40" height="36" viewBox="0 0 40 36"><path d="M20 2L3 11h34z" fill="#0456a4"/><rect x="7" y="14" width="4" height="14" fill="#0456a4"/><rect x="15" y="14" width="4" height="14" fill="#0456a4"/><rect x="22" y="14" width="4" height="14" fill="#0456a4"/><rect x="29" y="14" width="4" height="14" fill="#0456a4"/><rect x="3" y="30" width="34" height="4" fill="#0456a4"/></svg>
      <h3>COMMERCIAL LAW</h3>
      <p>Practical advice on contracts, leases and everyday commercial matters, tailored to local businesses and explained in plain terms.</p>
      <span class="more">LEARN MORE</span>
    </article>
    <article class="card">
      <svg width="40" height="36" viewBox="0 0 40 36"><rect x="4" y="10" width="32" height="22" rx="2" fill="#0456a4"/><rect x="14" y="4" width="12" height="8" rx="1" fill="none" stroke="#0456a4" stroke-width="3"/><rect x="4" y="18" width="32" height="2" fill="#fff"/></svg>
      <h3>BUSINESS SALE AND PURCHASES</h3>
      <p>Guidance through every stage of buying or selling a business, from due diligence and negotiation to a smooth settlement.</p>
      <span class="more">LEARN MORE</span>
    </article>
    <article class="card">
      <svg width="40" height="36" viewBox="0 0 40 36"><rect x="9" y="2" width="22" height="32" fill="#0456a4"/><rect x="13" y="9" width="14" height="2" fill="#fff"/><rect x="13" y="15" width="14" height="2" fill="#fff"/><rect x="13" y="21" width="10" height="2" fill="#fff"/></svg>
      <h3>WILLS AND ESTATES</h3>
      <p>Clear wills, powers of attorney and estate administration that protect your family and give you lasting peace of mind.</p>
      <span class="more">LEARN MORE</span>
    </article>
  </div>
</section>

<section class="team-gallery">
  <div class="team">
    <h2 class="col-title">OUR TEAM</h2>
    <div class="member">
      <div class="member-photo" role="img" aria-label="Portrait photo of a team member"></div>
      <div><h4>NAME HEADING</h4><p>Principal solicitor with a focus on property, conveyancing and commercial work for clients across the region.</p></div>
    </div>
    <div class="member">
      <div class="member-photo" role="img" aria-label="Portrait photo of a team member"></div>
      <div><h4>NAME HEADING</h4><p>Supports clients with leases, business transfers and general legal advice, always with a friendly local approach.</p></div>
    </div>
    <div class="member">
      <div class="member-photo" role="img" aria-label="Portrait photo of a team member"></div>
      <div><h4>NAME HEADING</h4><p>Assists with wills, estates and succession planning, helping families prepare clearly for the years ahead.</p></div>
    </div>
  </div>
  <div class="gallery">
    <h2 class="col-title">OUR GALLERY</h2>
    <div class="gallery-grid">
      <div class="g1" role="img" aria-label="Photo of a gavel and law books"></div>
      <div class="g2" role="img" aria-label="Photo of a couple meeting with a solicitor"></div>
      <div class="g3" role="img" aria-label="Photo of legal documents on a desk"></div>
      <div class="g4" role="img" aria-label="Photo of a last will and testament form"></div>
    </div>
  </div>
</section>

<div class="map" role="img" aria-label="Street map showing the office location in Hamilton"></div>
<svg class="map-pin" width="28" height="40" viewBox="0 0 28 40"><path d="M14 0C6 0 0 6 0 14c0 10 14 26 14 26s14-16 14-26C28 6 22 0 14 0z" fill="#d9382c"/><circle cx="14" cy="14" r="5" fill="#fff"/></svg>

<section class="office">
  <h2>OUR OFFICE LOCATION</h2>
  <div class="office-details">
    <span><svg width="12" height="16" viewBox="0 0 28 40"><path d="M14 0C6 0 0 6 0 14c0 10 14 26 14 26s14-16 14-26C28 6 22 0 14 0z" fill="#fff"/></svg>17 Pellow Road, Hamilton VIC 3300</span>
    <span><svg width="13" height="13" viewBox="0 0 24 24"><path fill="#fff" d="M6.6 10.8a15 15 0 006.6 6.6l2.2-2.2a1 1 0 011-.25 11.4 11.4 0 003.6.57 1 1 0 011 1V20a1 1 0 01-1 1A17 17 0 013 4a1 1 0 011-1h3.5a1 1 0 011 1c0 1.25.2 2.45.57 3.57a1 1 0 01-.25 1z"/></svg>(03) 5598 4731</span>
    <span><svg width="14" height="13" viewBox="0 0 24 22"><rect x="2" y="8" width="20" height="12" fill="#fff"/><rect x="6" y="1" width="12" height="8" fill="none" stroke="#fff" stroke-width="2"/></svg>(03) 5598 4706</span>
    <span><svg width="14" height="11" viewBox="0 0 24 18"><rect width="24" height="18" fill="#fff"/><path d="M1 1l11 9 11-9" stroke="#33a6d7" stroke-width="2" fill="none"/></svg>ross.kedwick@brindelllegal-example.com.au</span>
  </div>
</section>

<footer class="site-footer">
  <div>
    <div class="brand"><span class="brand-mark"></span>Brindell Legal</div>
    <div class="legal">Copyright © 2016. All Rights Reserved<br>Terms of Services</div>
  </div>
  <div class="follow">Follow Us On <span class="social"></span><span class="social s2"></span><span class="social s3"></span></div>
</footer>

</body>
</html>
```